Glimmerseal pond linings website template

We need a template for our new website. Glimmerseal is currently marketed through www.tarpavale.com.au, and we are moving the pond/dam linings to a dedicated site www.glimmerseal.com.au

The site is essentially brochureware. The content (less landing page & photo gallery) is on the new site to give you a better idea of what we do. We are also on Facebook.com/glimmerseal

We are looking for a template/style which we can adapt to the different sections of the site as required. We also get a lot of phone/tablet visitors so an alternative mobile layout would be a bonus, but by no means required.

I am proficient in HTML/CSS & javascript so can code most designs thrown at me.

Any icons or interface fonts should be freely available web fonts where possible.

Target Market(s)

We are targeting both landscape professionals (design & construction) as well as the DIY market for ponds/wateragrdens.

Industry/Entity Type

Moving

Requirements
Must have
• We need a design (preferably layered PSD or AI) as basis for our overall site look and feel. Fonts/iconography/layout are where we are lacking. We can do the HTML/CSS/JS/PHP internally.
Nice to have
• A style guide either in file or separate would be nice.
Layers with effect (i.e.. :hover, CSS3 transition endpoints, etc)

```html
<!DOCTYPE html>
<html lang="en">
<head>
<meta charset="utf-8">
<title>Glimmerseal — Pond Linings</title>
<link rel="stylesheet" href="https://fonts.googleapis.com/css2?family=Ubuntu:wght@400;500;700&family=Open+Sans:wght@400;600&display=swap">
<style>
:root{
  --navy:#0e3a78;
  --green:#1f8a4c;
  --lime:#a6c93a;
  --orange:#f07c12;
  --page:#eeeeef;
  --text:#444;
  --white:#fff;
}
*{box-sizing:border-box;margin:0;padding:0}
html,body{width:768px;height:1200px;overflow:hidden}
body{background:var(--page);font-family:"Open Sans",sans-serif;color:var(--text);position:relative}
.abs{position:absolute}
.brand{left:120px;top:14px;display:flex;align-items:center;gap:7px}
.brand-mark{width:30px;height:30px;background:var(--green)}
.brand-name{font-family:"Ubuntu",sans-serif;font-weight:500;font-size:19px;color:var(--green);letter-spacing:.5px}
.social{display:flex;gap:2px}
.social span{width:19px;height:19px;background:var(--green);display:block}
.social span:nth-child(2){background:var(--lime)}
.header-social{left:467px;top:27px}
.search{left:532px;top:28px;width:116px;height:17px;border:1px solid var(--green);background:var(--white);display:flex}
.search input{flex:1;border:0;font-size:6px;padding-left:6px;color:#999;font-family:inherit;background:none;outline:none}
.search button{width:20px;border:0;background:var(--green);display:flex;align-items:center;justify-content:center}
.nav{left:120px;top:64px;width:528px;height:27px;background:var(--navy);display:flex;padding-left:6px}
.nav a{color:var(--white);font-family:"Ubuntu",sans-serif;font-size:8.5px;text-decoration:none;padding:0 9.5px;line-height:27px;text-transform:uppercase}
.nav a.active{background:var(--lime);color:var(--navy);padding:0 13px}
.hero{left:120px;top:91px;width:528px;height:279px;background:linear-gradient(180deg,#4f6b3c 0%,#6b8a4a 40%,#5a6a4a 62%,#d98b3c 75%,#f0a050 100%);box-shadow:0 8px 10px -6px rgba(0,0,0,.35)}
.hero-copy{position:absolute;left:0;right:0;top:105px;text-align:center;color:var(--white);text-shadow:0 1px 3px rgba(0,0,0,.6)}
.hero-copy h1{font-family:"Ubuntu",sans-serif;font-weight:700;font-size:21px}
.hero-copy p{font-size:12px;line-height:13.5px;margin-top:6px}
.hero-cta{position:absolute;left:189px;top:176px;width:151px;height:23px;background:var(--orange);color:var(--white);font-family:"Ubuntu",sans-serif;font-weight:500;font-size:12px;display:flex;align-items:center;justify-content:center;clip-path:polygon(5% 0,95% 0,100% 50%,95% 100%,5% 100%,0 50%)}
.hero-arrow{position:absolute;top:130px;width:22px;height:22px;border-radius:50%;background:rgba(255,255,255,.25)}
.dots{position:absolute;left:245px;top:260px;display:flex;gap:3px}
.dots span{width:7px;height:7px;border:1.5px solid var(--white)}
.dots span.on{background:var(--navy)}
.intro{left:120px;top:396px;width:528px;text-align:center;font-size:12px;line-height:14.5px;color:var(--navy)}
.intro b{color:var(--orange)}
.section-title{left:120px;width:528px;display:flex;align-items:center;justify-content:center;gap:5px;font-family:"Ubuntu",sans-serif;font-weight:700;font-size:14.5px;color:var(--navy)}
.section-title::before,.section-title::after{content:"";width:60px;height:2px;background:var(--navy);opacity:.8}
.card{top:493px;width:169px;height:232px;background:var(--white);border-top:3px solid var(--green);box-shadow:0 1px 2px rgba(0,0,0,.15);padding:17px 18px 0}
.card.blue{border-top-color:var(--navy)}
.card h2{font-family:"Ubuntu",sans-serif;font-weight:500;font-size:15px;color:var(--green);display:flex;align-items:center;gap:5px}
.card.blue h2{color:var(--navy)}
.card h2 i{width:13px;height:13px;background:currentColor;display:block}
.card p{font-size:7.2px;line-height:9px;margin-top:6px;height:36px}
.card .photo{width:132px;height:67px;margin-top:1px}
.card ul{list-style:none;margin-top:7px}
.card li{font-size:7.5px;line-height:14.5px;display:flex;align-items:center;gap:5px}
.card li::before{content:"";width:4px;height:4px;border:1.3px solid var(--green)}
.card.blue li::before{border-color:var(--navy)}
.card .more{position:absolute;right:-3px;bottom:0;width:90px;height:16px;background:var(--orange);color:var(--white);font-size:8px;display:flex;align-items:center;justify-content:center;clip-path:polygon(10% 0,100% 0,100% 100%,0 100%)}
.thumb{top:796px;width:102px;height:72px;background:var(--white);border:1px solid #ddd;padding:5px}
.thumb div{width:100%;height:100%}
.caption{top:876px;width:102px}
.caption h3{font-family:"Ubuntu",sans-serif;font-weight:500;font-size:8.5px;color:var(--navy)}
.caption p{font-size:6.5px;line-height:7.5px;color:#222;margin-top:3px}
.contact{left:120px;top:930px;width:528px;height:195px;background:var(--white);border:1px solid #ddd}
.contact-info{position:absolute;left:5px;top:4px;width:191px;height:186px;background:var(--green);color:var(--white);padding:36px 0 0 28px}
.tag{display:flex;align-items:center;gap:4px;margin-bottom:3px}
.tag span{background:var(--lime);color:var(--green);font-size:6px;padding:1px 9px 1px 5px;clip-path:polygon(0 0,100% 0,88% 50%,100% 100%,0 100%)}
.contact-info p{font-size:8.5px;line-height:11.5px;margin-bottom:12px}
.contact-info .phone{font-family:"Ubuntu",sans-serif;font-size:14.5px}
.map{position:absolute;left:196px;top:4px;width:327px;height:186px;background:linear-gradient(135deg,#e8ecd8,#dfe6d0 50%,#b9d3ea 75%,#e4ead6)}
.map-pin{position:absolute;left:138px;top:56px}
.footer-links{left:120px;top:1144px;font-size:6.3px;line-height:8px;color:#333}
.footer-social{left:589px;top:1142px}
</style>
</head>
<body>
<header>
  <div class="abs brand"><span class="brand-mark"></span><span class="brand-name">GLIMMERSEAL</span></div>
  <div class="abs social header-social"><span></span><span></span><span></span></div>
  <form class="abs search"><input value="SEARCH" aria-label="Search"><button type="button" aria-label="Search"><svg width="8" height="8" viewBox="0 0 10 10"><circle cx="4" cy="4" r="3" fill="none" stroke="#fff" stroke-width="1.5"/><line x1="6.2" y1="6.2" x2="9" y2="9" stroke="#fff" stroke-width="1.5"/></svg></button></form>
  <nav class="abs nav">
    <a href="#">Home</a><a href="#">About Us</a><a href="#" class="active">Happenings</a><a href="#">Gallery</a><a href="#">Liner Styles</a><a href="#">Preparation</a><a href="#">Installation</a><a href="#">Contact Us</a>
  </nav>
</header>

<section class="abs hero" role="img" aria-label="Garden pond with waterfall, ferns and a timber deck">
  <span class="hero-arrow" style="left:20px"></span>
  <span class="hero-arrow" style="right:20px"></span>
  <div class="hero-copy">
    <h1>Glimmerseal Lorem Ipsum Dummy Slogan</h1>
    <p>Sed id ligula adipiscing purus lacinia aliquet. Sed eu est non nisl<br>vehicula bibendum congue sit amet enim.</p>
  </div>
  <a class="hero-cta">Get in Touch with</a>
  <div class="dots"><span></span><span class="on"></span><span></span><span></span></div>
</section>

<p class="abs intro">Glimmerseal has been manufactured, marketed and installed throughout Australia and the Pacific<br>Rim since the early 1980's for a variety of domestic and commercial applications. <b>&#10140;</b></p>

<h2 class="abs section-title" style="top:450px">WHAT WE DO?</h2>

<article class="abs card" style="left:120px">
  <h2><i></i>Liner Styles</h2>
  <p>Glimmerseal pond liners can be made to suit any size or shape pond you can imagine, from a small feature...</p>
  <div class="photo" role="img" aria-label="Stone path beside a lit garden pond" style="background:linear-gradient(135deg,#7d8aa0,#4a5468 60%,#5a3e3a)"></div>
  <ul><li>Flat Sheet Liners</li><li>Composite Liners</li><li>Profile Liners</li><li>Special Project Liners</li></ul>
  <a class="more">View all details</a>
</article>
<article class="abs card blue" style="left:298px">
  <h2><i></i>Preparation</h2>
  <p>Like most things, correct preparation of your pond prior to the installation of your Glimmerseal...</p>
  <div class="photo" role="img" aria-label="Excavated pond site in a grassy yard" style="background:linear-gradient(180deg,#6b6e52,#9a8a5e 50%,#b59c6a)"></div>
  <ul><li>Regulations</li><li>Excavation</li><li>Overflow &amp; Filling</li><li>Reticulation Systems</li></ul>
  <a class="more">View all details</a>
</article>
<article class="abs card" style="left:477px">
  <h2><i></i>Installation</h2>
  <p>Installing your Glimmerseal pond liner is an easy task, unfortunately there is no one single correct way to ...</p>
  <div class="photo" role="img" aria-label="Black liner edged with stacked stones" style="background:linear-gradient(180deg,#2e3440,#6e6a60 45%,#2a2e36)"></div>
  <ul><li>Standard Installation</li><li>Folding Corners</li><li>Pipes &amp; Penetrations</li><li>Edge Finishing</li></ul>
  <a class="more">View all details</a>
</article>

<h2 class="abs section-title" style="top:762px">OUR LANDSCAPES</h2>

<div class="abs thumb" style="left:120px"><div role="img" aria-label="Shopfront with potted plants" style="background:linear-gradient(180deg,#5a5040,#8a8070)"></div></div>
<div class="abs thumb" style="left:226.5px"><div role="img" aria-label="Garden bed with palms and sculpture" style="background:linear-gradient(180deg,#8a9a7a,#6a8a4a)"></div></div>
<div class="abs thumb" style="left:333px"><div role="img" aria-label="Flower display at a store entrance" style="background:linear-gradient(180deg,#4a3a30,#9a5a4a)"></div></div>
<div class="abs thumb" style="left:439.5px"><div role="img" aria-label="Landscaped courtyard with bench" style="background:linear-gradient(180deg,#8a7a6a,#7a8a5a)"></div></div>
<div class="abs thumb" style="left:546px"><div role="img" aria-label="Topiary garden sculpture on a street" style="background:linear-gradient(180deg,#9aa0a8,#4a6a3a)"></div></div>

<div class="abs caption" style="left:120px"><h3>H2 Heading Photo 1</h3><p>Nulla non neque. Phasellus libero magna...</p></div>
<div class="abs caption" style="left:227px"><h3>Landscape Photo 1</h3><p>Nulla non neque. Phasellus libero magna...</p></div>
<div class="abs caption" style="left:334px"><h3>Landscape Photo 1</h3><p>Nulla non neque. Phasellus libero magna...</p></div>
<div class="abs caption" style="left:440px"><h3>Landscape Photo 1</h3><p>Nulla non neque. Phasellus libero magna...</p></div>
<div class="abs caption" style="left:547px"><h3>Landscape Photo 1</h3><p>Nulla non neque. Phasellus libero magna...</p></div>

<section class="abs contact">
  <div class="contact-info">
    <div class="tag"><svg width="6" height="8" viewBox="0 0 6 8"><path d="M3 8 0.5 3.5A2.5 2.5 0 1 1 5.5 3.5Z" fill="#a6c93a"/></svg><span>POSTAL</span></div>
    <p>PO Box 2718, Fernbrook North,<br>Victoria, 3391, Australia</p>
    <div class="tag"><svg width="6" height="8" viewBox="0 0 6 8"><path d="M3 8 0.5 3.5A2.5 2.5 0 1 1 5.5 3.5Z" fill="#a6c93a"/></svg><span>FACTORY</span></div>
    <p>14-18 Kestrel Way, Hollowmere,<br>Victoria, 3391 Australia</p>
    <div class="tag"><svg width="7" height="7" viewBox="0 0 10 10"><path d="M2 0 4 3 3 4Q4.5 6.5 6 7L7 6 10 8 8.5 10Q3 9.5 0 2Z" fill="#a6c93a"/></svg><span>CALL US</span></div>
    <p class="phone">8200 - 555 -014</p>
  </div>
  <div class="map" role="img" aria-label="Road map of the region around the factory">
    <svg class="map-pin" width="38" height="52" viewBox="0 0 38 52"><path d="M19 50 4 28A17 17 0 1 1 34 28Z" fill="#fff" stroke="#0e3a78" stroke-width="3"/><text x="19" y="25" text-anchor="middle" font-family="Ubuntu,sans-serif" font-weight="700" font-size="12" fill="#0e3a78">GS</text></svg>
  </div>
</section>

<footer>
  <p class="abs footer-links">Home &nbsp;|&nbsp; About Us &nbsp;|&nbsp; Happenings &nbsp;|&nbsp; Gallery &nbsp;|&nbsp; Liner Styles &nbsp;|&nbsp; Preparation &nbsp;|&nbsp; Installation &nbsp;|&nbsp; Contact Us<br>Copyright © 2013 - Terms and Conditions</p>
  <div class="abs social footer-social"><span></span><span></span><span></span></div>
</footer>
</body>
</html>
```